FixyFellas,com Home Maintenance Membership Website

Fixy Fellas is a yearly home maintenance membership website where Home Owners, Contractor, and Subcontractors can interact in an online bidding environment to exchange goods and services.

Our Tag Line Is: We Tackle The Weekend Lists That Other Fellas Won't Tackle
Updates

Target Market(s)

Homeowner, Female, 26 to 56 years of age. Middle to upper income.
Contractors/Subcontractors

Industry/Entity Type

Environment

Font styles to use
Other font styles liked:
• We want to match the logo font

Requirements
Must have
• Three-tiered membership plans for homeowners. Features and pricing TBD
Three major customer components as well as a administration back end. The three main components will be Home Owners Page, Contractors/Subcontractors pages, and the request-for Work Pages.
Need Membership levels panel similar to the uploaded picture
We did like this site as a start point. http://www.coatguardprime.example/
Nice to have
• #1: Customer domain profiles for contractors
#2: Blog
#3: Affiliate Program
#4: Contractor Rating System
#5: Internal Messaging System
#6: Banner Ads
#7: Escrow Payments

```html
<!DOCTYPE html>
<html lang="en">
<head>
<meta charset="utf-8">
<title>Fixy Fellas – Home Maintenance Membership</title>
<link rel="stylesheet" href="https://fonts.googleapis.com/css2?family=Lato:wght@400;700;900&family=Alfa+Slab+One&display=swap">
<style>
:root{
  --orange:#fa5a00;
  --navy:#2e3a4b;
  --ink:#27323f;
  --muted:#9aa3ad;
  --line:#e6e8eb;
  --soft:#f4f5f7;
  --topbar:#111214;
  --footer:#3a3a3a;
  --white:#ffffff;
}
*{box-sizing:border-box;margin:0;padding:0}
html,body{width:1200px;height:2541px;overflow:hidden}
body{position:relative;background:var(--white);font-family:'Lato',sans-serif;color:var(--ink)}
.abs{position:absolute}

/* top bar */
.topbar{left:0;top:0;width:1200px;height:41px;background:var(--topbar);border-top:3px solid #2a2c33;color:#fff;font-size:12px}
.topbar .item{position:absolute;top:13px}
.topbar .sep{position:absolute;top:0;width:1px;height:38px;background:#333}
.lang-box{display:inline-block;width:18px;height:18px;background:#ddd;vertical-align:middle;margin-left:10px}
.socials{position:absolute;right:108px;top:12px;display:flex;gap:12px}
.socials span{width:13px;height:13px;border-radius:50%;background:#e9e9e9;display:block}

/* header */
.header{left:0;top:41px;width:1200px;height:134px;background:var(--white)}
.brand{position:absolute;left:127px;top:30px;display:flex;align-items:center;gap:10px}
.brand-dot{width:62px;height:62px;border-radius:50%;background:var(--ink)}
.brand-name{font-weight:900;font-size:22px;color:var(--orange)}
.nav{position:absolute;left:343px;top:56px;display:flex;gap:0}
.nav a{font-size:14px;color:#9aa3ad;text-decoration:none;width:77px;display:block}
.nav a.active{color:var(--orange);position:relative}
.nav a.active::before{content:"";position:absolute;left:0;top:-56px;width:36px;height:4px;background:var(--orange)}
.search{position:absolute;left:1076px;top:52px}

/* hero */
.hero{left:0;top:175px;width:1200px;height:508px;background:linear-gradient(120deg,#d9b98a 0%,#caa06b 25%,#6f94c8 50%,#4f7dbd 70%,#a3a8ad 100%)}
.hero-kicker{position:absolute;left:242px;top:197px;font-weight:900;font-size:21px;letter-spacing:2px;color:#111}
.hero-title{position:absolute;left:120px;top:220px;font-weight:900;font-size:55px;letter-spacing:3px;color:#111}
.hero-title .mark{position:relative}
.hero-title .mark::after{content:"";position:absolute;left:4px;right:-2px;top:28px;height:4px;background:var(--orange)}

/* features */
.feature{top:730px;width:300px}
.feature .icon{position:absolute;left:0;top:6px;width:30px;height:30px;background:var(--navy);transform:rotate(45deg)}
.feature h3{position:absolute;left:58px;top:0;font-size:15px;font-weight:700;color:var(--ink)}
.feature p{position:absolute;left:58px;top:28px;width:230px;font-size:11.5px;line-height:20px;color:var(--muted)}
.btn-orange{display:block;background:var(--orange);color:#fff;font-size:11.5px;text-align:center}
.feature .btn-orange{position:absolute;left:58px;top:101px;width:86px;height:30px;line-height:30px}

/* welcome */
.welcome{left:0;top:898px;width:1200px;height:339px;background:var(--soft)}
.welcome .photo{position:absolute;left:98px;top:48px;width:489px;height:251px;background:linear-gradient(180deg,#efefef 0%,#d8b37a 45%,#c99352 70%,#5c6f8f 100%)}
.welcome h2{position:absolute;left:614px;top:44px;font-size:27px;font-weight:900;letter-spacing:1.5px;color:var(--ink)}
.welcome p{position:absolute;left:614px;width:490px;font-size:11.5px;line-height:20px;color:var(--muted)}
.btn-outline{position:absolute;left:614px;top:234px;width:144px;height:41px;border:1px solid #d8dbe0;background:#fff;font-size:13px;font-weight:900;line-height:39px;text-align:center;color:var(--ink)}

/* section headings */
.sec-title{font-size:28px;font-weight:900;letter-spacing:1.5px;color:var(--ink);text-align:center}
.sec-sub{font-size:11.5px;line-height:20px;color:var(--muted);text-align:center}

/* pricing */
.plan{top:1387px;width:231px;height:400px;border:1px solid var(--line);background:#fff}
.plan .head{height:45px;background:var(--orange);color:#fff;font-weight:900;font-size:20px;letter-spacing:1.5px;text-align:center;line-height:45px}
.plan .price{height:44px;background:#eceeef;text-align:center;line-height:44px;color:var(--ink);font-size:12px}
.plan .price b{font-size:24px;font-weight:400}
.plan .price sup{font-size:11px}
.plan ul{list-style:none}
.plan li{height:34px;line-height:34px;border-bottom:1px solid var(--line);text-align:center;font-size:11px;color:var(--muted)}
.plan .buy{position:absolute;left:29px;top:346px;width:172px;height:38px;line-height:38px;font-weight:900;font-size:13px}
.plan.featured{border:3px solid var(--navy)}
.plan.featured .head{background:var(--navy)}
.plan.featured .price{background:var(--orange);color:#fff}
.plan.featured .buy{background:var(--navy)}
.hot{position:absolute;right:-3px;top:-3px;width:0;height:0;border-top:38px solid #7a8390;border-left:38px solid transparent}

/* rating */
.rating{left:864px;top:1381px;width:231px;height:316px;border:1px solid var(--line);background:#fff}
.rating .head{height:47px;background:var(--navy);color:#fff;font-size:12.5px;line-height:47px;padding-left:16px;position:relative}
.rating .head svg{position:absolute;right:18px;top:16px}
.rating .photo{position:absolute;left:15px;top:53px;width:201px;height:119px;background:linear-gradient(180deg,#b7d3ea 0%,#e8c36a 45%,#384a6b 100%)}
.rating h4{position:absolute;left:17px;top:204px;font-size:15px;font-weight:700}
.rating .stars{position:absolute;left:17px;top:230px;color:var(--orange);font-size:13px;letter-spacing:2px}
.rating .detail{position:absolute;left:64px;top:281px;width:90px;height:24px;background:#c5cad0;color:#fff;font-size:11px;line-height:24px;text-align:center}
.badge{left:864px;top:1712px;width:231px;height:70px;background:#c5ccd3;border-radius:3px}
.badge span{position:absolute;left:14px;top:12px;width:46px;height:46px;border-radius:50%;background:#2a4a6b}

/* blog */
.post{top:1944px;width:463px;height:166px;background:var(--soft)}
.post .strip{position:absolute;left:0;top:0;width:34px;height:166px;background:#5a6270}
.post .strip i{display:block;height:34px;border-bottom:1px solid #7a818c}
.post .strip i.on{background:var(--orange)}
.post .date{position:absolute;left:0;top:102px;width:34px;text-align:center;color:#fff;font-size:13px;font-weight:700;line-height:16px}
.post .date small{display:block;font-size:9px;font-weight:400}
.post .photo{position:absolute;left:34px;top:0;width:197px;height:166px}
.post h4{position:absolute;left:248px;top:14px;font-size:15px;font-weight:700}
.post .cat{position:absolute;left:248px;top:38px;font-size:11px;color:var(--muted)}
.post p{position:absolute;left:248px;top:60px;width:200px;font-size:11.5px;line-height:20px;color:var(--muted)}

/* ad banner */
.ad{left:134px;top:2153px;width:929px;height:144px;background:#c8c8c8;border:1px solid #b4b4b4;font-family:'Alfa Slab One',serif;font-size:40px;text-align:center;line-height:144px;color:#244b8f}
.ad .hl{color:var(--orange)}

/* footer */
.footer{left:0;top:2322px;width:1200px;height:219px;background:var(--footer);color:#fff;border-bottom:5px solid var(--orange)}
.footer .f-brand{position:absolute;left:127px;top:40px;display:flex;align-items:center;gap:8px}
.footer .f-brand span{width:56px;height:56px;border-radius:50%;background:#1d1d1d}
.footer .f-brand b{font-weight:900;font-size:20px;color:var(--orange)}
.f-social{position:absolute;left:148px;top:150px;display:flex;gap:14px}
.f-social span{width:11px;height:11px;border-radius:50%;background:#ddd}
.f-col{position:absolute;top:30px}
.f-col h5{font-size:17px;font-weight:700;padding-bottom:8px;position:relative}
.f-col h5::after{content:"";position:absolute;left:0;bottom:0;width:127px;height:2px;background:var(--orange)}
.f-col .row{font-size:11px;line-height:16px;margin-top:12px;display:flex;gap:10px}
.f-col .res{font-size:11px;margin-top:12px}
.f-col .res::before{content:"»";margin-right:10px}
.f-col .res.on{color:var(--orange)}
.f-col p{font-size:11px;line-height:16px;margin-top:10px;width:190px}
.f-input{margin-top:10px;width:187px;height:30px;border:1px solid var(--orange);background:#2f2f2f;color:#aaa;font-size:10px;line-height:28px;padding-left:8px}
.f-sub{position:absolute;left:114px;top:162px;width:72px;height:26px;background:var(--orange);font-size:11px;text-align:center;line-height:26px}
</style>
</head>
<body>

<div class="abs topbar">
  <div class="item" style="left:139px">Languages: <b>English</b><span class="lang-box"></span></div>
  <div class="sep" style="left:296px"></div>
  <div class="item" style="left:322px">Call us: 1.555.014.2290</div>
  <div class="sep" style="left:453px"></div>
  <div class="item" style="left:493px">hello@fixyfellas.example</div>
  <div class="sep" style="left:643px"></div>
  <div class="socials"><span></span><span></span><span></span><span></span><span></span><span></span><span></span><span></span><span></span><span></span></div>
</div>

<header class="abs header">
  <div class="brand"><span class="brand-dot"></span><span class="brand-name">Fixy Fellas</span></div>
  <nav class="nav">
    <a class="active">Home</a><a>Page</a><a>Portfolio</a><a>Blog</a><a>Shop</a><a>Travel</a><a style="width:100px">Shortcodes</a><a style="width:84px">Features</a><a>Contact</a>
  </nav>
  <svg class="search" width="26" height="26" viewBox="0 0 26 26"><circle cx="10" cy="10" r="8" fill="none" stroke="#9aa3ad" stroke-width="3"/><line x1="16" y1="16" x2="24" y2="24" stroke="#9aa3ad" stroke-width="3"/></svg>
</header>

<section class="abs hero" role="img" aria-label="Builder in a hard hat framing a timber roof against a blue sky">
  <div class="hero-kicker">WE ARE ALWAYS WORKING HARD TO</div>
  <div class="hero-title">BUILD T<span class="mark">HE</span> REAL VALUE</div>
</section>

<div class="abs feature" style="left:147px">
  <span class="icon"></span><h3>Fast Online Support</h3>
  <p>Praesent turpis mauris, aliquet id dolor Gravida adipiscing lectus ut rutrum Aenean at posuere risus.</p>
  <span class="btn-orange">Read more</span>
</div>
<div class="abs feature" style="left:475px">
  <span class="icon"></span><h3>Services</h3>
  <p>Praesent turpis mauris, aliquet id dolor Gravida adipiscing lectus ut rutrum Aenean at posuere risus.</p>
  <span class="btn-orange">Read more</span>
</div>
<div class="abs feature" style="left:802px">
  <span class="icon"></span><h3>Affiliate Program</h3>
  <p>Praesent turpis mauris, aliquet id dolor Gravida adipiscing lectus ut rutrum Aenean at posuere risus.</p>
  <span class="btn-orange">Read more</span>
</div>

<section class="abs welcome">
  <div class="photo" role="img" aria-label="Worker wearing a leather tool belt"></div>
  <h2>WELCOME TO FIXY FELLAS</h2>
  <p style="top:90px">Lorem ipsum dolor sit amet, consectetur adipiscing elit. Duis ut lobortis nulla. Vestibulum ante ipsum primis in faucibus orci luctus et ultrices posuere cubilia.</p>
  <p style="top:152px">Phasellus ut condimentum diam, eget tempus lorem. Morbi bibendum est quis arcu posuere condimentum. Nullam justo eros, pellentesque a metus non, mattis volutpat libero. Praesent ornare felis ante, sit amet porta felis pellentesque fermentum.</p>
  <div class="btn-outline">VIEW MORE &#8250;</div>
</section>

<h2 class="abs sec-title" style="left:330px;width:300px;top:1262px">PRICING TABLE</h2>
<p class="abs sec-sub" style="left:280px;width:400px;top:1304px">Our design is coupled with the excellent value<br>Aliquam sit amet hendrerit non, placerat pulvinar enim</p>
<h2 class="abs sec-title" style="left:880px;width:200px;top:1262px">RATING</h2>
<p class="abs sec-sub" style="left:860px;width:240px;top:1304px">Our design is coupled with the excellen-<br>value Aliquam sit amet hendrerit non,<br>placerat pulvinar enim</p>

<div class="abs plan" style="left:114px">
  <div class="head">BASIC</div>
  <div class="price"><sup>$</sup><b>99</b>/month</div>
  <ul><li>1 Hosting</li><li>2 Email Marketing</li><li>5 databases</li><li>2 Design Pack</li><li>3 Website Layouts</li><li>5 Header Style</li><li>3 Online Store</li></ul>
  <span class="btn-orange buy">BUY NOW</span>
</div>
<div class="abs plan" style="left:363px">
  <div class="head">ULTIMATE</div>
  <div class="price"><sup>$</sup><b>199</b>/month</div>
  <ul><li>1 Hosting</li><li>2 Email Marketing</li><li>5 databases</li><li>2 Design Pack</li><li>3 Website Layouts</li><li>5 Header Style</li><li>3 Online Store</li></ul>
  <span class="btn-orange buy">BUY NOW</span>
</div>
<div class="abs plan featured" style="left:611px;top:1384px;width:236px;height:406px">
  <span class="hot"></span>
  <div class="head" style="height:48px;line-height:48px">STANDARD</div>
  <div class="price"><sup>$</sup><b>299</b>/month</div>
  <ul><li>1 Hosting</li><li>2 Email Marketing</li><li>5 databases</li><li>2 Design Pack</li><li>3 Website Layouts</li><li>5 Header Style</li><li>3 Online Store</li></ul>
  <span class="btn-orange buy" style="left:30px;top:348px">BUY NOW</span>
</div>

<div class="abs rating">
  <div class="head">Contractor Rating
    <svg width="18" height="14" viewBox="0 0 18 14"><path d="M1 5 L5 1 H13 L17 5 L9 13 Z M1 5 H17" fill="none" stroke="#fff" stroke-width="1.5"/></svg>
  </div>
  <div class="photo" role="img" aria-label="Group of contractors in hard hats"></div>
  <h4>Contractor Rating</h4>
  <div class="stars">★★★★☆</div>
  <div class="detail">View detail</div>
</div>
<div class="abs badge"><span></span></div>

<h2 class="abs sec-title" style="left:300px;width:600px;top:1828px">RECENT POST FROM BLOG</h2>
<p class="abs sec-sub" style="left:400px;width:400px;top:1871px">Our design is coupled with the excellent value<br>Aliquam sit amet hendrerit non, placerat pulvinar enim</p>

<article class="abs post" style="left:125px">
  <div class="strip"><i class="on"></i><i></i><i></i></div>
  <div class="date">24<small>Jan</small></div>
  <div class="photo" role="img" aria-label="Hands holding assorted hand tools" style="background:linear-gradient(135deg,#f2efe9 0%,#c9a06a 55%,#a84a2c 100%)"></div>
  <h4>Your Blog Title Here</h4>
  <div class="cat">Contractor</div>
  <p>Donec mattis felis sit amet viverra elementum. Nullam rutrum sit amet nisl eu rhoncus. Duis tristique dolor magna, vitae mattis mauris</p>
</article>
<article class="abs post" style="left:614px">
  <div class="strip"><i class="on"></i><i></i><i></i></div>
  <div class="date">24<small>Jan</small></div>
  <div class="photo" role="img" aria-label="Worker holding a power drill" style="background:linear-gradient(135deg,#e6e6e6 0%,#b58356 50%,#3c4a5e 100%)"></div>
  <h4>Your Blog Title Here</h4>
  <div class="cat">Contractor</div>
  <p>Donec mattis felis sit amet viverra elementum. Nullam rutrum sit amet nisl eu rhoncus. Duis tristique dolor magna, vitae mattis mauris</p>
</article>

<div class="abs ad">Advertise <span class="hl">Your Business</span> Here!</div>

<footer class="abs footer">
  <div class="f-brand"><span></span><b>Fixy Fellas</b></div>
  <div class="f-social"><span></span><span></span><span></span><span></span><span></span></div>

  <div class="f-col" style="left:385px">
    <h5>Contact</h5>
    <div class="row">
      <svg width="9" height="12" viewBox="0 0 9 12"><path d="M4.5 0 A4.5 4.5 0 0 1 9 4.5 C9 8 4.5 12 4.5 12 C4.5 12 0 8 0 4.5 A4.5 4.5 0 0 1 4.5 0 Z" fill="#fff"/><circle cx="4.5" cy="4.5" r="1.6" fill="#3a3a3a"/></svg>
      <span>418 Cedar Row, Suite 7<br>&nbsp;&nbsp;Brookfield,<br>&nbsp;&nbsp;OR 97000</span>
    </div>
    <div class="row">
      <svg width="10" height="10" viewBox="0 0 10 10"><path d="M2 0 L4 2.5 L3 4 C4 6 5 7 6 7.5 L7.5 6.5 L10 8.5 L8.5 10 C4 9.5 0.5 6 0 1.5 Z" fill="#fff"/></svg>
      <span>1300 555 014</span>
    </div>
    <div class="row">
      <svg width="11" height="8" viewBox="0 0 11 8"><rect x="0.5" y="0.5" width="10" height="7" fill="none" stroke="#fff"/><path d="M0.5 0.5 L5.5 4.5 L10.5 0.5" fill="none" stroke="#fff"/></svg>
      <span>info@fixyfellas.example</span>
    </div>
  </div>

  <div class="f-col" style="left:625px">
    <h5>Resources</h5>
    <div class="res on">Repairs &amp; Maintenance</div>
    <div class="res">Carpentary</div>
    <div class="res">Fencing</div>
    <div class="res">Out Doors</div>
  </div>

  <div class="f-col" style="left:868px">
    <h5 style="padding-bottom:4px">Subscribe</h5>
    <p>Subscribe to our newsletter to receive news, updates, free stuff and new releases by email. We don't do spam.</p>
    <div class="f-input">Enter your email address</div>
    <svg style="position:absolute;left:8px;top:162px" width="30" height="22" viewBox="0 0 30 22"><rect x="1" y="4" width="26" height="16" fill="#eee" transform="rotate(-8 14 12)"/><path d="M2 5 L14 13 L27 2" fill="none" stroke="#999" stroke-width="1"/></svg>
    <div class="f-sub">Subscribe</div>
  </div>
</footer>

</body>
</html>
```